Medical Internet Marketing Company Needs a Site!

We need a new, fresh website for our search engine optimization and social media marketing company. We specialize in helping medical practices, doctors, physicians, and hospitals with their online presence and web ranking. The site should lean towards being suited for these audiences.

We have several examples of website that we like as well as things that we like about them.

Here are sites that we enjoy.

www.brightwavelab.com

It's a good design for the site all around. The videos, buttons, and images are all excellent. They did a fine job.

- We really like their "contact us" side bar and want to include one like it on the secondary pages.

www.corvantis.net

- We don't like the "thickness" of the top navigation bar.
- We like the page colors, easy navigation, and big call to action phone number in the top right corner.

http://www.teluvo.com/

Out of all the examples provided, Teluvo is our favorite and closest look and style to what we are looking for.

- We really like the openness of the design, such as space between the text and background.

- We want a price page in a style very similar to their pricing page with the services listed and check-marks, etc. although we intend to have multiple service package columns much like Corvantis's SEO pricing page.

- The way the video fits into the home page header is very organized, simple, and attention grabbing. We intend to place a slider with videos here.

- We need a page design that will allow for an image slider like Teluvo's Features page.

Here's a great example of a medical internet marketing website: http://www.dermaplex.com/

Target Market(s)

Our target market is doctors, typically male and typically 40-45 years old. I

Industry/Entity Type

Marketing

Requirements
Must have
• The homepage should have a slider in the video. Interior pages should have a video in the very top similar to how they do it on www.brightwavelab.com

The top navigation tabs needed are:
- Home
- Solutions
- Resources
- About
- Why Quelvo
- Contact

The sidebar should have a GREAT call to action in it on interior pages.

There should be one interior page that is similar to this - http://www.teluvo.com/pricing/

There needs to be a page with multiple boxes that take up a row of the web page's body. This page will house all the case studies similar to brightwave lab's: http://www.brightwavelab.com/success-stories/case-studies/ The one exception is we want the case studies to be inside of "boxes" instead of between horizontal lines like brightwave lab's.
Nice to have
• Color, professional, and clean. GREAT use of calls to actions.

```html
<!DOCTYPE html>
<html lang="en">
<head>
<meta charset="utf-8">
<title>Quelvo – Medical Internet Marketing</title>
<link href="https://fonts.googleapis.com/css2?family=Arimo:wght@400;700&family=Questrial&family=PT+Sans:ital@1&family=Noto+Serif:ital@1&family=Montserrat:wght@700&display=swap" rel="stylesheet">
<style>
:root{
  --blue:#2a93cf;
  --blue-dark:#1a7db9;
  --sky:#7fd0f2;
  --frame:#f1b56d;
  --ink:#333;
  --muted:#666;
  --light:#f2f2f2;
  --card:#ececec;
  --bar:#3b3b3b;
  --green:#8cc63f;
  --footer:#050505;
  --line:#d8d8d8;
}
*{box-sizing:border-box;margin:0;padding:0}
html,body{width:1050px;height:1200px;overflow:hidden}
body{position:relative;background:#f7f7f7 repeating-linear-gradient(90deg,#f9f9f9 0 3px,#f3f3f3 3px 4px);font-family:Arimo,Arial,sans-serif;color:var(--ink)}
.abs{position:absolute}

/* header */
.site-header{left:0;top:0;width:1050px;height:64px;background:#fff;border-bottom:1px solid #ddd}
.brand{left:154px;top:20px;display:flex;align-items:center;gap:10px;font-family:Arimo,Arial,sans-serif;font-size:26px;letter-spacing:3px;color:#7b8087}
.brand-mark{width:22px;height:22px;background:var(--blue)}
.main-nav{left:453px;top:0;display:flex;height:63px}
.main-nav a{display:block;padding:18px 11px 0;text-decoration:none;color:#222;font-size:12px;text-transform:uppercase;height:63px}
.main-nav a.current{background:#f2f2f2}
.main-nav small{display:block;font-size:9px;font-style:italic;color:#b5b5b5;text-transform:none;margin-top:5px}

/* hero */
.hero{left:0;top:64px;width:1050px;height:272px;background:linear-gradient(180deg,#2c9bd6,#1f86c4);border-bottom:4px solid #1b74ab}
.promo-title{left:150px;top:137px;width:172px;height:35px;background:var(--sky);color:#fff;font-family:'PT Sans',sans-serif;font-style:italic;font-size:21px;padding:5px 0 0 12px;letter-spacing:1px}
.promo-box{left:150px;top:172px;width:300px;height:42px;background:#fff;font-family:'Noto Serif',serif;font-size:10px;line-height:15px;padding:6px 10px;color:#333}
.promo-go{left:450px;top:172px;width:49px;height:42px;background:var(--sky)}
.specialty-btn{left:150px;top:261px;width:274px;height:43px;background:linear-gradient(#2d2d2d,#111);color:#fff;font-family:Montserrat,sans-serif;font-size:13px;letter-spacing:.5px;padding:14px 0 0 11px;border-radius:3px;box-shadow:0 3px 6px rgba(0,0,0,.35)}
.video-frame{left:529px;top:84px;width:371px;height:217px;background:var(--frame);padding:8px}
.video-photo{width:100%;height:100%;background:linear-gradient(135deg,#e9edf0,#c9d2d8 60%,#f4f4f4)}
.slider-dots{left:700px;top:311px;display:flex;gap:6px}
.slider-dots span{width:9px;height:9px;border-radius:50%;background:#7bc2e8}
.slider-dots span.on{background:#fff}

/* hello band */
.hello-band{left:0;top:338px;width:1050px;height:170px;background:linear-gradient(#f4f4f4,#e6e6e6);border:1px solid #ccc}
.hello-badge{left:150px;top:351px;width:114px;height:114px;border-radius:50%;background:var(--sky);color:#fff;font-family:Questrial,sans-serif;font-size:33px;display:flex;align-items:center;justify-content:center}
.hello-badge span{transform:rotate(-15deg)}
.hello-headline{left:299px;top:352px;width:620px;font-family:Questrial,sans-serif;font-size:40px;line-height:46px;color:#3a3a3a}

/* intro */
.intro-text{left:150px;top:525px;width:548px;font-family:'PT Sans',sans-serif;font-style:italic;font-size:16.5px;line-height:23px;color:#444;text-align:justify}
.intro-photo{left:734px;top:518px;width:180px;height:128px;background:#fff;padding:8px;transform:rotate(-4deg);box-shadow:0 2px 6px rgba(0,0,0,.3)}
.intro-photo div{width:100%;height:100%;background:linear-gradient(135deg,#8a6a40,#3e8f8a 55%,#cfd9d8)}

/* cards */
.card{top:702px;width:235px;height:265px;background:var(--card);border-bottom:1px solid #ccc}
.card-title{height:31px;background:var(--bar);color:#fff;font-family:'Noto Serif',serif;font-style:italic;font-size:20px;text-align:right;padding:3px 10px 0 0}
.card-image{height:149px}
.card-text{font-size:10.5px;line-height:15px;color:#555;padding:6px 7px 0;text-align:justify}
.card-link{display:flex;align-items:center;gap:8px;font-size:10.5px;color:#333;padding:10px 0 0 9px}
.card-link i{width:18px;height:18px;border-radius:50%;background:#fff;display:flex;align-items:center;justify-content:center}
.events{left:665px;top:702px;width:235px;height:265px;background:var(--card);border-top:5px solid var(--green);border-bottom:1px solid #ccc}
.events h3{font-family:'Noto Serif',serif;font-style:italic;font-weight:400;font-size:20px;text-align:center;height:33px;padding-top:5px}
.event-item{display:flex;gap:9px;height:69px;padding:11px 9px;border-bottom:1px solid var(--line);font-size:10.5px;line-height:14px;color:#444}
.event-thumb{flex:0 0 70px;height:47px;background:linear-gradient(135deg,#7a5a3a,#2f9a96 60%,#dde)}
.view-all{font-size:10px;text-align:right;padding:7px 15px 0 0;color:#555;letter-spacing:.5px}

/* bottom row */
.section-title{font-family:Questrial,sans-serif;font-size:18px;color:#333}
.quote-box{left:150px;top:1036px;width:368px;height:61px;background:#fff;border:1px solid #e3e3e3;border-radius:0 0 14px 14px;padding:10px 14px 0 55px;font-size:9px;line-height:13px;color:#444}
.quote-author{left:466px;top:1111px;font-style:italic;font-size:14px;color:#222}
.pager{left:868px;top:1015px;font-size:13px;color:#999;letter-spacing:8px}
.text-box{left:613px;top:1036px;width:287px;height:84px;background:#fff;border:1px solid #bbb;border-radius:3px;padding:10px 11px;font-size:9px;line-height:15px;color:#444;text-align:justify}

/* footer */
.site-footer{left:0;top:1139px;width:1050px;height:61px;background:var(--footer)}
.footer-nav{left:150px;top:1152px;display:flex;gap:22px;font-size:11px;color:#6d6d6d}
.footer-legal{left:154px;top:1180px;font-size:10px;color:#555}
.social{left:755px;top:1151px;display:flex;gap:8px}
.social span{width:26px;height:26px;border-radius:50%;background:#3c3c3c}
</style>
</head>
<body>

<header class="site-header abs"></header>
<div class="brand abs"><span class="brand-mark"></span>QUELVO</div>
<nav class="main-nav abs">
  <a class="current" href="#">Home<small>back to</small></a>
  <a href="#">Solutions<small>what we offer</small></a>
  <a href="#">Resources<small>what we do</small></a>
  <a href="#">About<small>our selfs</small></a>
  <a href="#">Why Quelvo<small>company</small></a>
  <a href="#">Contact<small>get us</small></a>
</nav>

<section class="hero abs"></section>
<div class="promo-title abs">LOREM IPSUM</div>
<p class="promo-box abs">Lorem ipsum dolor sit amet, consectetuer adipiscing elit.Aenean commodo ligula eget dolor. Aenean massa.</p>
<div class="promo-go abs">
  <svg width="49" height="42" viewBox="0 0 49 42"><path d="M15 21h19M28 15l6 6-6 6" stroke="#fff" stroke-width="1.6" fill="none"/></svg>
</div>
<div class="specialty-btn abs">SELECT YOUR SPECIALTY TO VIEW</div>
<div class="video-frame abs">
  <div class="video-photo" role="img" aria-label="Video still of a smiling medical team in white coats"></div>
</div>
<svg class="abs" style="left:720px;top:168px" width="16" height="26" viewBox="0 0 16 26"><path d="M0 0L14 13 0 26z" fill="#111"/></svg>
<div class="slider-dots abs"><span class="on"></span><span></span><span></span></div>

<section class="hello-band abs"></section>
<div class="hello-badge abs"><span>Hello!</span></div>
<h1 class="hello-headline abs" style="font-weight:400">Lorem ipsum dolor sit amet, con­sectetuer adipiscing elit. Aenean commodo ligula eget dolor.</h1>

<p class="intro-text abs">Lorem ipsum dolor sit amet, consectetuer adipiscing elit. Aenean commodo ligula eget dolor. Aenean massa. Cum sociis natoque penatibus et magnis dis parturient montes, nascetur ridiculus mus. Donec quam felis, ultricies nec, pellentesque eu, pretium quis, sem. Nulla consequat massa quis enim. Donec pede justo, fringilla vel, aliquet nec, vulputate eget, arcu.</p>
<div class="intro-photo abs"><div role="img" aria-label="Photo of doctors and nurses working together"></div></div>

<article class="card abs" style="left:150px">
  <h2 class="card-title" style="font-weight:400">Doctor Portal</h2>
  <div class="card-image" role="img" aria-label="Photo of a doctor reading a tablet" style="background:linear-gradient(135deg,#e6e6e6,#f7f7f7 50%,#2d8fc4)"></div>
  <p class="card-text">Lorem ipsum dolor sit amet, consectetuer adipiscing elit. Aenean commodo ligula eget dolor.</p>
  <div class="card-link">EXPLORE <i><svg width="8" height="8" viewBox="0 0 8 8"><path d="M2 1l3 3-3 3" stroke="#333" fill="none"/></svg></i></div>
</article>
<article class="card abs" style="left:408px">
  <h2 class="card-title" style="font-weight:400">Press</h2>
  <div class="card-image" role="img" aria-label="Photo of a dart on a newspaper page" style="background:linear-gradient(135deg,#c9c9c9,#f2f2f2 45%,#4a4a4a)"></div>
  <p class="card-text">Lorem ipsum dolor sit amet, consectetuer adipiscing elit. Aenean commodo ligula eget dolor.</p>
  <div class="card-link">EXPLORE <i><svg width="8" height="8" viewBox="0 0 8 8"><path d="M2 1l3 3-3 3" stroke="#333" fill="none"/></svg></i></div>
</article>
<aside class="events abs">
  <h3>Events</h3>
  <div class="event-item"><div class="event-thumb" role="img" aria-label="Event photo of medical staff"></div><p>Lorem ipsum dolor sit amet, consectetuer adipiscing</p></div>
  <div class="event-item"><div class="event-thumb" role="img" aria-label="Event photo of medical staff"></div><p>Lorem ipsum dolor sit amet, consectetuer adipiscing</p></div>
  <div class="event-item"><div class="event-thumb" role="img" aria-label="Event photo of medical staff"></div><p>Lorem ipsum dolor sit amet, consectetuer adipiscing</p></div>
  <div class="view-all">VIEW ALL</div>
</aside>

<h2 class="section-title abs" style="left:154px;top:1004px;font-weight:400">What other say's</h2>
<blockquote class="quote-box abs">Lorem ipsum dolor sit Lorem ipsum dolor sit amet, consectetuer adipiscing elit. Aenean commodo ligula eget dolor. amet, consectetuer adAenean commodo ligula eget dolor.</blockquote>
<svg class="abs" style="left:160px;top:1046px" width="34" height="26" viewBox="0 0 34 26"><path d="M2 26V12L10 0h4L9 12h6v14zM19 26V12L27 0h4l-5 12h6v14z" fill="#e6e6e6"/></svg>
<div class="quote-author abs">- Marcus</div>

<h2 class="section-title abs" style="left:613px;top:1004px;font-weight:400">Some text</h2>
<div class="pager abs">‹ ›</div>
<p class="text-box abs">Lorem ipsum dolor sit Lorem ipmet, consectetuer adipiscing elit. Aenean commodo ligula esum dolor sit amet, consectetuer adipiscing elit. Aenean commodo ligula eget dolor. amet, consectetuer adAenean commodo ligula eget dolor.</p>

<footer class="site-footer abs"></footer>
<nav class="footer-nav abs"><span>Home</span><span>Solutions</span><span>Resources</span><span>About</span><span>Why Quelvo</span><span>Contact</span></nav>
<p class="footer-legal abs">© 2012 quelvo.com &nbsp;|&nbsp; T&amp;C</p>
<div class="social abs"><span></span><span></span><span></span><span></span></div>

</body>
</html>
```